Poster Needed for Church Conference

I need a poster for a weekend conference at my church. Looking to attract as many people as possible. We are a church in the suburbs of Houston. This is mainly for our own church members but we are opening it up to outside church members.

Please see previous design from last conference and all other graphic work that can (doesn't need to be) included.

Target Market(s)

It's targeted for all people. But our main audience is families. around the age of 30 should be main target.

Industry/Entity Type

Non-Profit

Font styles to use
Serif
Sans Serif

Colors

Designer to choose colors to be used in the design.

Requirements
Must have
• 11x17 design with ability to shrink and blow up. but ideally for 11x17
• Content and wording:
• "Rooted Lantern Conference: Bridging the gap between generations and passing on our deepest beliefs and values."
• Featuring Dr. Glen Marlowe. Author of "The Map of Q9"
• Aug 25-26: Friday 8-10 pm, Saturday 4-8 pm
• Cost Adults $15/Children $5: Covers admission to all sessions and workshops, refreshments and Saturday dinner. *kids 5 and under free
• Childcare provided for all sessions. "
• Please use church logo and address on flyer: 4312 Orchard Bend, Missouri City, TX 77512
Nice to have
• Ideally it will be designed so that we can crop a 16:9 pp announcement slide and header for our website.
Should not have
• anything offensive

```html
<!DOCTYPE html>
<html lang="en">
<head>
<meta charset="utf-8">
<title>Rooted Lantern Conference Poster</title>
<link href="https://fonts.googleapis.com/css2?family=League+Spartan:wght@600;700&family=Open+Sans:wght@300;400;600;700&display=swap" rel="stylesheet">
<style>
  :root {
    --page-bg: #e8ecee;
    --charcoal: #2b2d2d;
    --white: #ffffff;
    --ink: #1c1c1c;
    --lime: #62e61c;
    --lime-name: #5fe01a;
    --note: #c6ec0e;
    --pin: #d8202a;
    --photo-green: #5ef11a;
  }
  * { margin: 0; padding: 0; box-sizing: border-box; }
  html, body { width: 1200px; height: 1200px; overflow: hidden; }
  body { background: var(--page-bg); position: relative; font-family: "Open Sans", Arial, sans-serif; }

  .poster {
    position: absolute; left: 233px; top: 38px;
    width: 734px; height: 1123px;
    background: var(--white); overflow: hidden;
    box-shadow: 0 10px 30px rgba(0,0,0,0.18);
  }
  .poster > * { position: absolute; }

  .title-band {
    left: 0; top: 0; width: 734px; height: 252px;
    background: var(--charcoal); color: var(--white);
    font-family: "League Spartan", "Helvetica Neue", sans-serif; font-weight: 600;
    text-align: center;
  }
  .title-band .line { position: absolute; left: 0; width: 100%; line-height: 1; }
  .title-band .line-one { top: 28px; font-size: 92px; letter-spacing: -1px; }
  .title-band .line-two { top: 140px; font-size: 96px; }

  .speaker-photo { left: 76px; top: 280px; width: 206px; height: 234px; background: var(--photo-green); }

  .featuring { left: 324px; top: 276px; width: 328px; text-align: right;
    font-family: "League Spartan", sans-serif; font-weight: 700; font-size: 31px; color: var(--ink); }
  .speaker-name { left: 324px; top: 317px; white-space: nowrap;
    font-family: "League Spartan", sans-serif; font-weight: 700; font-size: 44px; color: var(--lime-name); }
  .author-credit { left: 324px; top: 370px;
    font-family: "League Spartan", sans-serif; font-weight: 700; font-size: 25px; line-height: 36.5px; color: var(--ink); }

  .book-cover { left: 538px; top: 378px; width: 104px; height: 150px; transform: skewY(-6deg);
    background: linear-gradient(135deg, #f4f5f4 0%, #dfe2e0 60%, #c9ccca 100%);
    box-shadow: 3px 4px 6px rgba(0,0,0,0.25); }
  .book-cover::after { content: ""; position: absolute; left: 0; right: 0; top: 90px; height: 14px; background: var(--lime); }

  .tagline-band { left: 0; top: 542px; width: 734px; height: 90px; background: var(--charcoal);
    color: var(--white); font-weight: 600; font-size: 23.5px; line-height: 35px;
    padding: 10px 14px 0 12px; text-indent: 34px; }

  .childcare { left: 304px; top: 652px; width: 430px; height: 49px; background: var(--charcoal);
    color: var(--white); font-weight: 300; font-size: 25px; line-height: 49px; padding-left: 13px; white-space: nowrap; }

  .price { width: 148px; height: 148px; border-radius: 50%; background: var(--lime);
    color: var(--white); font-family: "League Spartan", sans-serif; font-weight: 600;
    font-size: 32px; line-height: 38px; text-align: center; padding-top: 36px; }
  .price-children { left: 26px; top: 705px; }
  .price-adults { left: 181px; top: 705px; }

  .pin { width: 26px; height: 34px; }

  .church-tag { left: 551px; top: 767px; width: 183px; height: 49px; background: var(--charcoal);
    display: flex; align-items: center; padding-left: 14px; gap: 12px; }
  .church-tag .church-name { color: var(--lime); font-size: 11.5px; font-weight: 600; line-height: 14px; }

  .coverage { left: 41px; top: 869px; width: 680px; font-size: 22.5px; line-height: 34px; color: var(--ink); }

  .note { width: 248px; height: 175px; background: var(--note); box-shadow: 2px 3px 5px rgba(0,0,0,0.25);
    text-align: center; font-size: 25px; line-height: 37px; color: var(--ink); padding-top: 40px; }
  .note-address { left: 110px; top: 968px; transform: rotate(-1deg); }
  .note-dates { left: 366px; top: 961px; transform: rotate(1deg); padding-top: 35px; line-height: 39px; }
</style>
</head>
<body>
  <main class="poster">
    <header class="title-band">
      <h1>
        <span class="line line-one">Rooted Lantern</span>
        <span class="line line-two">Conference</span>
      </h1>
    </header>

    <div class="speaker-photo" role="img" aria-label="Portrait photo of speaker Dr. Glen Marlowe on a green background"></div>
    <p class="featuring">Featuring</p>
    <h2 class="speaker-name">Dr. Glen Marlowe</h2>
    <p class="author-credit">Author<br>of<br>The<br>The Map of Q9</p>
    <div class="book-cover" role="img" aria-label="Cover of the book The Map of Q9"></div>

    <p class="tagline-band">Bridging the gap between generations and passing on our deepest beliefs and values.</p>

    <p class="childcare">Childcare provided for all sessions</p>

    <div class="price price-children">Children<br>$5</div>
    <div class="price price-adults">Adults<br>$15</div>
    <svg class="pin" style="left:82px;top:696px" viewBox="0 0 26 34"><line x1="14" y1="16" x2="18" y2="32" stroke="#8a8a8a" stroke-width="2"/><circle cx="12" cy="11" r="9" fill="var(--pin)"/></svg>
    <svg class="pin" style="left:237px;top:696px" viewBox="0 0 26 34"><line x1="14" y1="16" x2="18" y2="32" stroke="#8a8a8a" stroke-width="2"/><circle cx="12" cy="11" r="9" fill="var(--pin)"/></svg>

    <div class="church-tag">
      <svg width="16" height="18" viewBox="0 0 16 18"><polygon points="0,0 16,9 0,18" fill="var(--white)"/></svg>
      <span class="church-name">Cedar Hollow<br>Community Church</span>
    </div>

    <p class="coverage">Covers admission to all sessions and workshops, refreshments and&nbsp; Saturday dinner.</p>

    <div class="note note-address">4312 Orchard Bend,<br>Missouri City,<br>TX 77512</div>
    <div class="note note-dates">Aug 25-26<br>Friday 8-10 pm<br>Saturday 4-8 pm</div>
    <svg class="pin" style="left:206px;top:958px" viewBox="0 0 26 34"><line x1="14" y1="16" x2="18" y2="32" stroke="#8a8a8a" stroke-width="2"/><circle cx="12" cy="11" r="9" fill="var(--pin)"/></svg>
    <svg class="pin" style="left:472px;top:951px" viewBox="0 0 26 34"><line x1="14" y1="16" x2="18" y2="32" stroke="#8a8a8a" stroke-width="2"/><circle cx="12" cy="11" r="9" fill="var(--pin)"/></svg>
  </main>
</body>
</html>
```